Redesign Charity Golf Outing Flyer

We need a redesign of our current golf outing flyer. The charity is in the name of a fallen police officer and the funds help scholarships for future police officers and community projects. I have included the artwork from last year. We brand everything with "The Spark 47" because Gordon's badge number was 182 and he often told people he was "The Spark". The details on the flyer will need to be editable (we have access to the full Adobe creative suite). While the cause is serious the event itself is fun so feel free to have fun with it.

Target Market(s)

Golfers and people who want to donate.

Industry/Entity Type

Charity

Font styles to use
Sans Serif

Colors
0555a3

Requirements
Must have
• All information included on last years flyer.
Nice to have
• A modern feel.
Should not have
• N/a

```html
<!DOCTYPE html>
<html lang="en">
<head>
<meta charset="utf-8">
<title>2nd Annual Gordon D. Hale Memorial &amp; Scholarship Golf Scramble</title>
<link rel="stylesheet" href="https://fonts.googleapis.com/css2?family=Oswald:wght@400&family=Open+Sans:ital,wght@0,400;0,600;0,700;1,700&family=Libre+Baskerville:wght@700&display=swap">
<style>
  :root{
    --blue:#35619a;
    --blue-text:#2b5d9e;
    --pill-blue:#1f63b0;
    --orange:#f26a1f;
    --black:#0e0e0e;
    --charcoal:#262626;
    --white:#ffffff;
    --ink:#1b1b1b;
    --grey-text:#4a4a4a;
  }
  *{box-sizing:border-box;margin:0;padding:0}
  html,body{width:900px;height:1200px;overflow:hidden;background:#f2f2f2}
  body{font-family:"Open Sans",Arial,sans-serif;color:var(--ink)}
  .flyer{position:relative;width:900px;height:1200px;background:var(--white);overflow:hidden}

  .hero-photo{position:absolute;left:0;top:0;width:900px;height:490px;
    background:linear-gradient(160deg,#d8ecc0 0%,#9ccc5a 35%,#5e9a2a 70%,#3f7a1c 100%)}
  .orange-strip{position:absolute;left:0;top:490px;width:540px;height:32px;
    background:linear-gradient(180deg,#f47a30,#e2591a)}

  .brand-name{position:absolute;left:36px;top:52px;font-family:"Open Sans",sans-serif;font-weight:700;
    font-size:30px;line-height:1;color:var(--ink)}

  .header-band{position:absolute;left:364px;top:0;width:536px;height:156px;background:var(--black);
    display:flex;align-items:center;padding-left:30px}
  .header-num{font-family:"Oswald",sans-serif;font-weight:400;font-size:112px;line-height:1;color:var(--orange);margin-right:6px}
  .header-title{font-family:"Oswald",sans-serif;font-weight:400;font-size:39px;line-height:1.08;color:var(--white)}

  .side-column{position:absolute;left:534px;top:156px;width:366px;height:1044px;background:var(--charcoal)}
  .info-panel{position:absolute;left:551px;top:156px;width:329px;height:885px;background:var(--blue);
    border:2px solid #5f86b8;text-align:center;color:var(--white)}
  .remember{font-family:"Libre Baskerville",serif;font-size:26px;margin-top:22px;line-height:1.2}
  .remember .bar{color:var(--orange)}
  .portrait{display:block;margin:14px auto 0;width:158px;height:160px;border:6px solid #1e8fe0;
    background:linear-gradient(180deg,#e8e8e8 0%,#bdbdbd 55%,#2a2a2a 56%,#111 100%)}
  .event-name{font-size:34px;font-weight:400;margin-top:22px;line-height:1.1}
  .event-day{color:var(--orange);font-size:22px;margin-top:6px;font-weight:400}
  .event-date{display:inline-block;background:var(--orange);color:var(--white);font-weight:700;font-size:21px;padding:1px 12px;margin-top:2px}
  .time{font-size:20px;margin-top:8px}
  .walkup{color:var(--orange);font-size:15px;font-weight:600;line-height:1.45;margin-top:2px}
  .divider{width:190px;height:2px;background:var(--orange);margin:10px auto 0}
  .venue{text-align:left;padding-left:42px;margin-top:12px;position:relative}
  .venue-name{color:var(--orange);font-size:17px}
  .venue-line{font-size:13px;line-height:1.5}
  .phone{font-weight:700;font-size:15px;margin-top:12px;display:flex;align-items:center;gap:10px}
  .icon{width:18px;height:18px;flex:none}
  .venue .icon-home{position:absolute;left:14px;top:2px}

  .fee-box{position:absolute;left:536px;top:864px;width:336px;height:72px;background:var(--orange);color:var(--white);font-size:16px}
  .fee-line{padding:8px 0 0 12px}
  .fee-line b{color:var(--black);font-weight:400}
  .includes{display:flex;align-items:center;margin-top:4px}
  .includes-pill{background:var(--pill-blue);padding:1px 10px;border-radius:0 14px 14px 0;margin-right:8px}

  .register{position:absolute;left:551px;top:972px;width:329px;text-align:center;color:var(--white)}
  .register-lead{font-size:20px}
  .register-url{font-size:14px;font-weight:700;margin-top:2px}

  .contact-block{position:absolute;left:551px;top:1041px;width:329px;height:159px;background:var(--orange);color:var(--white)}
  .contact-pill{display:inline-block;background:var(--pill-blue);font-size:14px;padding:3px 50px 3px 10px;border-radius:0 16px 16px 0;margin-top:14px}
  .contact-body{position:relative;padding:12px 0 0 38px;font-size:14px;line-height:1.4}
  .contact-body .icon-home{position:absolute;left:10px;top:14px}
  .contact-body .phone{margin-left:-28px;margin-top:4px;font-size:14px}

  .form{position:absolute;left:0;top:532px;width:534px;padding:0 30px 0 66px}
  .form-title{font-size:21px;font-weight:600;color:var(--blue-text);text-align:center;height:32px}
  .field{display:flex;align-items:flex-end;height:32px;font-style:italic;font-weight:700;font-size:13px;padding-left:4px}
  .field .line{flex:1;border-bottom:2px dotted #555;margin:0 0 4px 10px}
  .field .short{flex:1.2}
  .field .mid{flex:.8}
  .field .gap{font-style:italic;margin-left:8px}
  .sponsor-head{font-size:20px;font-weight:600;color:var(--blue-text);line-height:1.4;margin-top:10px}
  .sponsor-field{font-size:13px;margin-top:6px;padding-left:4px}
  .sponsor-field small{font-size:11px}
  .dots{border-bottom:2px dotted #555;height:20px;margin-left:4px}
  .donation{display:flex;align-items:flex-end;font-size:13px;margin-top:10px;padding-left:4px}
  .donation .line{flex:1;border-bottom:2px dotted #555;margin:0 0 4px 10px}
  .deadline{color:var(--orange);font-weight:600;font-size:19px;margin-top:12px}
  .mail-note{color:var(--grey-text);font-weight:700;font-size:15px;line-height:1.45;margin-top:4px;white-space:nowrap}

  .mail-pill{position:absolute;left:56px;top:1070px;width:450px;height:34px;background:var(--pill-blue);border-radius:17px;
    color:var(--white);font-size:16px;font-weight:600;line-height:34px;padding-left:24px}
  .footer{position:absolute;left:0;top:1141px;width:534px;height:59px;background:var(--black);color:var(--white);
    text-align:center;font-weight:700;font-size:15px;line-height:59px}
</style>
</head>
<body>
<main class="flyer">
  <div class="hero-photo" role="img" aria-label="Golf ball and iron club resting on green grass"></div>
  <div class="orange-strip"></div>

  <p class="brand-name">The Spark 47</p>

  <header class="header-band">
    <span class="header-num">2</span>
    <h1 class="header-title">nd Annual Gordon D. Hale<br>Memorial &amp; Scholarship</h1>
  </header>

  <div class="side-column"></div>

  <section class="info-panel">
    <p class="remember">Remembering<br><span class="bar">|</span>The Spark<span class="bar">|</span></p>
    <div class="portrait" role="img" aria-label="Portrait of Officer Gordon D. Hale in uniform"></div>
    <h2 class="event-name">Golf Scramble</h2>
    <p class="event-day">Saturday-August</p>
    <p class="event-date">15, 2015</p>
    <p class="time">9am Registration</p>
    <p class="walkup">Day of scramble registrations<br>are welcome</p>
    <p class="time" style="margin-top:4px">10am Shotgun Start</p>
    <div class="divider"></div>
    <div class="venue">
      <svg class="icon icon-home" viewBox="0 0 20 20"><path d="M10 2 1 10h3v8h4v-5h4v5h4v-8h3z" fill="#f26a1f"/></svg>
      <p class="venue-name">Cedar Ridge Golf Course</p>
      <p class="venue-line">1480 Fairway Loop Rd.</p>
      <p class="venue-line">Brookfield, OH 44900</p>
      <p class="phone" style="margin-left:-28px">
        <svg class="icon" viewBox="0 0 20 20"><path d="M4 1h4l2 5-3 2c1 2 3 4 5 5l2-3 5 2v4c0 2-2 3-4 3C8 18 2 12 1 5c0-2 1-4 3-4z" fill="#f26a1f"/></svg>
        (555) 014-2290
      </p>
    </div>
  </section>

  <div class="fee-box">
    <p class="fee-line">Entry Fee: <b>$55</b>/person <b>($220/team)</b></p>
    <div class="includes"><span class="includes-pill">Includes:</span>Green fees, cart and dinner</div>
  </div>

  <div class="register">
    <p class="register-lead">Register below or online at:</p>
    <p class="register-url">www.spark47scramble.org</p>
  </div>

  <section class="contact-block">
    <span class="contact-pill">Any Questions Contact:</span>
    <div class="contact-body">
      <svg class="icon icon-home" viewBox="0 0 20 20"><path d="M10 2 1 10h3v8h4v-5h4v5h4v-8h3z" fill="#111"/></svg>
      <p>Dale Morton</p>
      <p>905 Maple Crest Lane</p>
      <p>Westbrook, OH 44901</p>
      <p class="phone">
        <svg class="icon" viewBox="0 0 20 20"><path d="M4 1h4l2 5-3 2c1 2 3 4 5 5l2-3 5 2v4c0 2-2 3-4 3C8 18 2 12 1 5c0-2 1-4 3-4z" fill="#111"/></svg>
        (555) 017-3364
      </p>
    </div>
  </section>

  <section class="form">
    <h2 class="form-title">Team Captian Information:</h2>
    <div class="field">Captain’s Name:<span class="line"></span></div>
    <div class="field">Address:<span class="line"></span></div>
    <div class="field">City:<span class="line short"></span><span class="gap">State:</span><span class="line mid"></span><span class="gap">Zip:</span><span class="line mid"></span></div>
    <div class="field">Captain’s Phone:<span class="line"></span></div>
    <div class="field">Captain’s Email:<span class="line"></span></div>
    <div class="field">Player # 2 Name:<span class="line"></span></div>
    <div class="field">Player # 2 Name:<span class="line"></span></div>
    <div class="field">Player # 4 Name:<span class="line"></span></div>

    <h3 class="sponsor-head">Can’t Make it or Don’t Golf?<br>Sponsor a hole/tee:</h3>
    <p class="sponsor-field">Name/Bussiness <small>(attach bussiness card if possible):</small></p>
    <div class="dots"></div>
    <div class="donation">Donation Amont:<span class="line"></span></div>
    <p class="deadline">Mail-in Deadline: August 1, 2015</p>
    <p class="mail-note">Mail this completed form with check(s) made payable to:<br>“The Officer Gordon D. Hale Memorial Scholarship Fund”</p>
  </section>

  <div class="mail-pill">Mail to contact information on the right.</div>
  <footer class="footer">www.spark47scramble.org</footer>
</main>
</body>
</html>
```